we need a homepage for a marketplace

We manage all projects using our ground-breaking platform Velbrim Portal. You get access to 150+ partners in 70 countries, security, cost efficiency, technical skills, speed, 100% visibility and accountability.Velbrim aims to help clients realize the full potential of their investments, provide a competitive price, establish the business need as a competitive advantage, and provide a strategic business asset that can facilitate growth.
Target Market(s)
Freelancers
Industry/Entity Type
Business Software
Number of Pages Required
1 page
Requirements
Must have
- Credentials -http://qlvtk.com/freelancer/public
- Front :
- Client:
- Email id - doriek@fallowquartzsystems.com
- Password - 123456
- Partner:
- Email id - mortenl@fallowquartzsystems.com
- Password - 123456
- Project Manager:
- Email id - lorcan@fallowquartzsystems.com
- Password - 123456
Nice to have
- It will be nice to have a creative design, and a outside the box look/feel

```html
<!DOCTYPE html>
<html lang="en">
<head>
<meta charset="utf-8">
<title>Velbrim Portal — Home</title>
<link href="https://fonts.googleapis.com/css2?family=Questrial&display=swap" rel="stylesheet">
<style>
:root{
  --hero:#2f4a86;
  --hero-dark:#223a70;
  --accent:#2a5bd7;
  --navy:#1d2d5a;
  --ink:#333;
  --muted:#777;
  --line:#aaa;
  --band:#dfdfdf;
  --foot:#595959;
  --foot-line:#6c6c6c;
  --base:#2b2b2b;
  --white:#fff;
}
*{margin:0;padding:0;box-sizing:border-box}
html,body{width:720px;height:1200px;overflow:hidden}
body{position:relative;font-family:"Questrial",sans-serif;color:var(--ink);background:var(--white)}
.abs{position:absolute}
/* hero */
.hero{position:absolute;left:0;top:0;width:720px;height:308px;background:linear-gradient(120deg,#3a5595 0%,var(--hero) 55%,var(--hero-dark) 100%);color:var(--white)}
.brand{position:absolute;left:0;top:0;width:96px;height:48px;background:var(--white);display:flex;align-items:center;justify-content:center;font-size:17px;color:var(--navy)}
.nav a{position:absolute;top:19px;font-size:8px;letter-spacing:.3px;color:var(--white);text-decoration:none}
.nav-underline{position:absolute;left:134px;top:45px;width:88px;height:2px;background:var(--accent)}
.pill{position:absolute;border:1px solid rgba(255,255,255,.7);border-radius:10px;font-size:7.5px;display:flex;align-items:center;justify-content:center;gap:5px}
.hero h1{position:absolute;left:98px;top:74px;font-weight:400;font-size:26px;line-height:36px}
.hero p{position:absolute;left:98px;top:181px;width:168px;font-size:6.5px;line-height:8px}
.cta{position:absolute;top:253px;height:19px;border:1px solid rgba(255,255,255,.7);border-radius:10px;font-size:10px;display:flex;align-items:center;justify-content:center}
/* steps */
.section-title{position:absolute;left:0;width:720px;text-align:center;font-weight:400;color:var(--navy)}
.step h3{font-weight:400;font-size:8.5px;color:var(--navy)}
.step p{font-size:6.4px;line-height:8px;color:var(--muted);width:100px;margin-top:1px}
/* industries */
.band{position:absolute;left:0;top:596px;width:720px;height:288px;background:var(--band)}
.service h3{font-weight:400;font-size:8.5px;color:var(--navy)}
.service p{font-size:6.4px;line-height:8.1px;color:var(--muted);width:98px;margin-top:1px}
.portrait{position:absolute;left:612px;top:696px;width:108px;height:188px;background:linear-gradient(180deg,#c9c9c9,#9a9a9a);border-radius:40px 40px 0 0}
/* footer */
.footer{position:absolute;left:0;top:884px;width:720px;height:240px;background:var(--foot);color:var(--white)}
.fcol{position:absolute;width:128px}
.fcol h4{font-weight:400;font-size:9.5px;padding-bottom:3px;border-bottom:1px solid var(--foot-line);margin-bottom:5px}
.fcol li{list-style:none;font-size:6.6px;line-height:9.4px}
.fcol p{font-size:6.6px;line-height:8.4px}
.field{height:16px;background:#6d6d6d;font-size:6.6px;padding-left:5px;display:flex;align-items:center;margin-top:7px}
.btn-ghost{border:1px solid #bbb;border-radius:9px;height:18px;display:flex;align-items:center;justify-content:center;font-size:9.5px}
.base{position:absolute;left:0;top:1124px;width:720px;height:76px;background:var(--base);color:#ddd;font-size:8.5px}
.base span{position:absolute;top:37px}
.sq{position:absolute;top:41px;width:4px;height:4px;background:var(--accent)}
</style>
</head>
<body>

<header class="hero" role="img" aria-label="Office desk and chair photo tinted in blue">
  <div class="brand">Velbrim</div>
  <nav class="nav">
    <a style="left:165px">HOME</a>
    <a style="left:251px">ABOUT US</a>
    <a style="left:355px">CONTACT US</a>
  </nav>
  <div class="nav-underline"></div>
  <div class="pill" style="left:571px;top:15px;width:65px;height:17px">ACCOUNT
    <svg width="10" height="6" viewBox="0 0 10 6"><path d="M1 1l4 4 4-4" fill="none" stroke="#2a5bd7" stroke-width="1.6"/></svg></div>
  <div class="pill" style="left:658px;top:15px;width:43px;height:17px">LOGOUT</div>
  <h1>Connect With.<br>Manage All.<br>Deliver To.</h1>
  <p><b>Velbrim</b> aims to help clients realize the full potential of their investments, provide a competitive price, establish the business need as a competitive advantage, and provide a strategic business asset that can facilitate growth.</p>
  <div class="cta" style="left:208px;width:120px">BECOME A PARTNER</div>
  <div class="cta" style="left:349px;width:120px">POST YOUR PROJECT</div>
</header>

<h2 class="section-title" style="top:329px;font-size:19px">HOW IT WORKS</h2>
<div class="section-title" style="top:355px;font-size:9.6px;color:var(--accent)">Organizations Can Benefit From Our Talent Pool In The Following East Steps</div>

<svg class="abs" style="left:0;top:390px" width="720" height="90" viewBox="0 0 720 90">
  <g fill="none" stroke="#999" stroke-width="1.6">
    <path d="M48 12V64H100"/><path d="M44 16l4-6 4 6"/>
    <path d="M160 64H262"/><path d="M298 64H408"/><path d="M452 64H560"/><path d="M606 64H660"/><path d="M655 60l5 4-5 4"/>
  </g>
  <g fill="none" stroke="#2c3a66" stroke-width="1.3">
    <rect x="106" y="48" width="47" height="29"/><path d="M104 80h51"/>
    <path d="M270 48h22l-5 10h-12z"/><path d="M281 60l4 8h9l-7 6 3 9-9-5-9 5 3-9-7-6h9z"/>
    <circle cx="430" cy="64" r="7"/><circle cx="430" cy="64" r="13" stroke-dasharray="5 3"/>
    <path d="M567 57l16-12 16 12v20h-32z"/><path d="M567 57l16 11 16-11"/><rect x="575" y="47" width="16" height="14"/>
  </g>
</svg>

<div class="abs step" style="left:82px;top:486px"><h3>Post Your Project</h3><p>Lorem ipsum dolor sit amet, consectetuer adipiscing elit, sed diam nonummy nibh euismod tincidunt</p></div>
<div class="abs step" style="left:233px;top:486px"><h3>Select an Expert</h3><p>Lorem ipsum dolor sit amet, consectetuer adipiscing elit, sed diam nonummy nibh euismod tincidunt</p></div>
<div class="abs step" style="left:383px;top:486px"><h3>Work on the Project</h3><p>Lorem ipsum dolor sit amet, consectetuer adipiscing elit, sed diam nonummy nibh euismod tincidunt</p></div>
<div class="abs step" style="left:534px;top:486px"><h3>Pay only when Satisfied</h3><p>Lorem ipsum dolor sit amet, consectetuer adipiscing elit, sed diam nonummy nibh euismod tincidunt</p></div>

<section class="band">
  <h2 class="section-title" style="top:26px;font-size:19px;line-height:23px">PROJECT MANAGER FOR EVERY BUSINESS<br>CHALLENGE ACROSS A WIDE RANGE OF INDUSTRIES</h2>
</section>
<div class="portrait" role="img" aria-label="Photo of a smiling project manager"></div>

<div class="abs service" style="left:82px;top:710px"><h3>Cloud Computing</h3><p>Locate your system in the cloud and access your information from any place or device with the highest security level....</p></div>
<div class="abs service" style="left:217px;top:710px"><h3>QA Testing</h3><p>We will help you find and eliminate problems &amp; bugs, enhance performance of your product and give another brush to logics and design....</p></div>
<div class="abs service" style="left:351px;top:710px"><h3>Consulting Services</h3><p>Should you need a consultation, training, troubleshooting or implementation of enhancements to your product, our team is always ready to help you!...</p></div>
<div class="abs service" style="left:486px;top:710px"><h3>Web Development</h3><p>Our goal is to bring the most recognizable and modern solutions to the world web market. We do our best in order to make your site usable, profitable and, what ...</p></div>
<div class="abs service" style="left:82px;top:796px"><h3>Web Design</h3><p>Our passion, dedication and your idea blend in elegant customized design that turns your project into success....</p></div>
<div class="abs service" style="left:217px;top:796px"><h3>Security &amp; Compliance</h3><p>Protect your information with best of our data security methods and techniques and build the trust of your customers!...</p></div>
<div class="abs service" style="left:351px;top:796px"><h3>Mobile App Development</h3><p>But I must explain to you how all this mistaken idea of denouncing pleasure and praising pain was born and I will give you a complete account of the system, and...</p></div>
<div class="abs service" style="left:486px;top:796px"><h3>Technical Support Services</h3><p>Outstaffing development teams is what nowadays makes IT one of the most scalable industries. We are not saying that traditional inhouse teams are replaced by fr...</p></div>

<footer class="footer">
  <div class="fcol" style="left:45px;top:13px"><h4>Industries</h4><ul><li>Financial Services</li><li>Retail</li><li>Nonprofit</li><li>Government</li><li>Life Sciences</li><li>Manufacturing</li><li>Healthcare</li><li>Real Estate</li><li>Communications</li><li>Higher Ed</li><li>Insurance</li></ul></div>
  <div class="fcol" style="left:218px;top:13px"><h4>Project Category</h4><ul><li>Cloud Computing</li><li>QA Testing</li><li>Consulting Services</li><li>Web Development</li><li>Web Design</li><li>Security &amp; Compliance</li><li>Mobile App Development</li><li>Technical Support Services</li></ul></div>
  <div class="fcol" style="left:390px;top:13px"><h4>About <b>VB</b></h4>
    <div style="font-size:20px;margin:8px 0 10px">Velbrim</div>
    <p style="width:145px">We are experienced and highly qualified software engineers, cloud architects, inventors, cyber security engineers and project managers.</p>
    <div class="btn-ghost" style="width:77px;margin-top:9px">Learn More</div></div>
  <div class="fcol" style="left:563px;top:13px;width:135px"><h4>Subscribe Newsletter</h4>
    <p>Get a weekly round-us of the top cloud computing news and views form Velbrim and more to help you stay ahead and make informed decisions.</p>
    <div class="field" style="margin-top:10px">Enter Your Name</div><div class="field">Enter Your Email</div>
    <div class="btn-ghost" style="width:77px;margin-top:6px">Subscribe</div></div>
  <div class="fcol" style="left:45px;top:157px"><h4>Support &amp; Downloads</h4><ul><li>Support Team</li><li>Support Ticket</li><li>Help</li><li>FAQ</li><li>Downloads</li><li>Contact Us</li></ul></div>
  <div class="fcol" style="left:218px;top:157px"><h4>Career</h4><ul><li>Internship</li><li>Career</li></ul></div>
  <div class="fcol" style="left:390px;top:157px"><h4>Blog</h4><ul><li>Latest</li><li>Most Populer</li><li>Likes</li></ul></div>
  <div class="fcol" style="left:563px;top:157px"><h4>Events</h4><ul><li>Latest</li><li>Career Events</li></ul></div>
</footer>

<div class="base">
  <span style="left:50px">Copyright 2016 <b>VELBRIM</b>. ALL Rights Reserved.</span>
  <span style="left:400px">Privacy Policy</span><i class="sq" style="left:476px"></i>
  <span style="left:503px">Terms &amp; Conditions</span><i class="sq" style="left:605px"></i>
  <span style="left:624px">Sitemap</span>
</div>

</body>
</html>
```